Flyer design for the Harvest Lantern Summit 2019 (HALSUM)

Design a flyer for our annual conference with basic information about the conference: conference logo and year, Conference name: Harvest Lantern Summit Location: Talbot Community Center (Downtown Portland)482 Wexley Street, Portland, ME 04109, Date: August 8th, 9th, 10th and 11th, 2019Start time 7:00PMI would like the following three words added to the flyer. These words describe the vision of the conference: Prophetic, Fire, Overflow,

Contact info:
Website: www.vostel.org
Phone: 207 555 3184
Email: contact@meadowcrest.org

Target Market(s)

Young adults living in the United States

Industry/Entity Type

Religious

Font styles to use
Sans Serif

Colors

Designer to choose colors to be used in the design.

Requirements
Must have
• HALSUM must logo standout, the reader should be able to take a quick look and find key info,
Should not have
• Cross image, church image

```html
<!DOCTYPE html>
<html lang="en">
<head>
<meta charset="utf-8">
<title>Harvest Lantern Summit 2019 Flyer</title>
<link rel="stylesheet" href="https://fonts.googleapis.com/css2?family=Montserrat:wght@700&family=Old+Standard+TT:wght@400&display=swap">
<style>
  :root {
    --backdrop: #2f93b3;
    --flyer-dark: #1c1915;
    --flyer-mid: #2a241c;
    --glow-amber: #b8741c;
    --glow-deep: #5a3a12;
    --gold: #f3d86a;
    --gold-pale: #f6e39a;
    --amber: #f0a52a;
    --frame: #e9b83a;
  }
  * { box-sizing: border-box; margin: 0; padding: 0; }
  html, body {
    width: 1200px;
    height: 886px;
    overflow: hidden;
    background: var(--backdrop);
  }
  .flyer {
    position: absolute;
    left: 305px;
    top: 33px;
    width: 590px;
    height: 820px;
    background: linear-gradient(180deg, var(--flyer-dark) 0%, var(--flyer-mid) 55%, #3a2c18 100%);
    overflow: hidden;
    font-family: "Old Standard TT", serif;
    text-align: center;
  }
  .sunset-scene {
    position: absolute;
    left: 0; right: 0; bottom: 0;
    height: 380px;
    background:
      radial-gradient(ellipse 70% 45% at 50% 88%, rgba(240,170,70,0.75), rgba(184,116,28,0.35) 55%, transparent 80%),
      linear-gradient(180deg, transparent 0%, var(--glow-deep) 55%, var(--glow-amber) 100%);
  }
  .gold-sweep {
    position: absolute;
    right: 0; top: 0;
    width: 340px;
    height: 100px;
    background: linear-gradient(160deg, transparent 20%, rgba(243,200,90,0.85) 45%, rgba(200,150,40,0.5) 60%, transparent 80%);
    opacity: 0.9;
  }
  .frame {
    position: absolute;
    border: 1px solid var(--frame);
    pointer-events: none;
  }
  .frame--outer { inset: 24px; }
  .frame--inner { inset: 33px; }
  .logo-name {
    position: absolute;
    left: 0; right: 0;
    top: 88px;
    font-family: "Montserrat", sans-serif;
    font-weight: 700;
    font-size: 76px;
    line-height: 1;
    letter-spacing: 1px;
    color: var(--gold);
  }
  .logo-year {
    position: absolute;
    left: 102px; right: 102px;
    top: 168px;
    display: flex;
    align-items: center;
    gap: 14px;
    font-family: "Montserrat", sans-serif;
    font-weight: 700;
    font-size: 30px;
    letter-spacing: 16px;
    color: var(--gold);
  }
  .logo-year::before, .logo-year::after {
    content: "";
    flex: 1;
    height: 2px;
    background: var(--gold);
  }
  .logo-year span { margin-right: -16px; }
  .event-title {
    position: absolute;
    left: 0; right: 0;
    top: 232px;
    font-size: 42px;
    line-height: 56px;
    font-weight: 400;
  }
  .event-title .lead { color: var(--amber); display: block; }
  .event-title .rest { color: var(--gold-pale); display: block; }
  .vision {
    position: absolute;
    left: 0; right: 0;
    top: 356px;
    font-size: 21px;
    letter-spacing: 0.5px;
    color: var(--amber);
  }
  .rule {
    position: absolute;
    left: 120px; right: 120px;
    height: 2px;
    background: var(--amber);
  }
  .rule--top { top: 396px; }
  .rule--bottom { top: 530px; }
  .month {
    position: absolute;
    left: 0; right: 0;
    top: 404px;
    font-size: 44px;
    color: var(--gold-pale);
  }
  .dates {
    position: absolute;
    left: 0; right: 0;
    top: 460px;
    font-size: 22px;
    color: var(--amber);
  }
  .venue {
    position: absolute;
    left: 0; right: 0;
    top: 494px;
    font-size: 14px;
    line-height: 1;
    color: var(--gold-pale);
    white-space: nowrap;
  }
  .start-label {
    position: absolute;
    left: 0; right: 0;
    top: 542px;
    font-size: 22px;
    color: var(--gold-pale);
  }
  .start-time {
    position: absolute;
    left: 0; right: 0;
    top: 568px;
    font-size: 48px;
    color: var(--gold-pale);
  }
  .contact {
    position: absolute;
    left: 74px;
    top: 653px;
    width: 442px;
    height: 104px;
    border: 2px solid var(--amber);
    display: flex;
    align-items: center;
    padding: 0 10px 0 14px;
  }
  .contact legend {
    margin: 0 auto;
    padding: 0 6px;
    font-size: 30px;
    line-height: 1;
    color: var(--gold-pale);
  }
  .contact-phone {
    display: flex;
    align-items: center;
    gap: 10px;
    font-size: 29px;
    letter-spacing: -0.5px;
    white-space: nowrap;
    color: var(--amber);
    padding-right: 12px;
    border-right: 1px solid var(--gold-pale);
    height: 44px;
    flex: none;
  }
  .contact-lines {
    display: flex;
    flex-direction: column;
    gap: 12px;
    padding-left: 12px;
    font-size: 11px;
    white-space: nowrap;
    color: var(--gold-pale);
    text-align: left;
  }
  .contact-lines div { display: flex; align-items: center; gap: 7px; }
  .icon { flex: none; }
</style>
</head>
<body>
  <article class="flyer">
    <div class="sunset-scene" role="img" aria-label="Silhouette of a person with raised arms against a golden sunset sky"></div>
    <div class="gold-sweep" role="img" aria-label="Sweeping gold light streaks with sparkles"></div>
    <div class="frame frame--outer"></div>
    <div class="frame frame--inner"></div>

    <h1 class="logo-name">HALSUM</h1>
    <div class="logo-year"><span>2019</span></div>

    <h2 class="event-title">
      <span class="lead">Harvest Lantern</span>
      <span class="rest">Summit</span>
    </h2>
    <p class="vision">PROPHETIC, FIRE, OVERFLOW</p>

    <div class="rule rule--top"></div>
    <p class="month">August</p>
    <p class="dates">8th, 9th, 10th and 11th 2019</p>
    <p class="venue">Talbot Community Center &middot; 482 Wexley Street, Portland, ME 04109</p>
    <div class="rule rule--bottom"></div>

    <p class="start-label">Start time</p>
    <p class="start-time">7:00PM</p>

    <fieldset class="contact">
      <legend>Contact info:</legend>
      <div class="contact-phone">
        <svg class="icon" width="22" height="22" viewBox="0 0 24 24" aria-hidden="true">
          <circle cx="12" cy="12" r="12" fill="#f0a52a"/>
          <path d="M8.2 6.5l2 .2 1 2.6-1.3 1.1a7 7 0 0 0 3.7 3.7l1.1-1.3 2.6 1 .2 2c-.4.8-1.2 1.3-2.1 1.2A10 10 0 0 1 7 8.6c-.1-.9.4-1.7 1.2-2.1z" fill="#2a241c"/>
        </svg>
        <span>207 555 3184</span>
      </div>
      <div class="contact-lines">
        <div>
          <svg class="icon" width="10" height="10" viewBox="0 0 10 10" aria-hidden="true"><circle cx="5" cy="5" r="5" fill="#f3d86a"/><rect x="2.5" y="3.2" width="5" height="3.6" fill="none" stroke="#2a241c" stroke-width="0.9"/></svg>
          <span>contact@meadowcrest.org</span>
        </div>
        <div>
          <svg class="icon" width="10" height="10" viewBox="0 0 10 10" aria-hidden="true"><circle cx="5" cy="5" r="5" fill="#f3d86a"/><path d="M1 5h8M5 1v8" stroke="#2a241c" stroke-width="0.8"/></svg>
          <span>www.vostel.org</span>
        </div>
      </div>
    </fieldset>
  </article>
</body>
</html>
```